TGCo Wholesale Flyer

I need a wholesaler flyer/letter put together. I've provided copy and a range of photos for the designer to use. The flyer needs to match the same colour pallet and style of tallowmeregoodsco.com.au.

It will be used to send to new potenial retailers so needs to look smick.

```html
<!DOCTYPE html>
<html lang="en">
<head>
<meta charset="UTF-8">
<title>Ingredients</title>
<link rel="stylesheet" href="https://fonts.googleapis.com/css2?family=Fraunces:opsz,wght@9..144,600&family=Montserrat:wght@400;700&display=swap">
<style>
  :root {
    --paper: #ffffff;
    --band: #dfe0db;
    --ink: #161616;
    --body-ink: #1e1e1e;
  }
  * { margin: 0; padding: 0; box-sizing: border-box; }
  html, body { width: 849px; height: 1200px; overflow: hidden; background: var(--paper); }
  .sheet { position: relative; width: 849px; height: 1200px; background: var(--paper); }
  .section-band {
    position: absolute; left: 0; width: 849px; height: 49px;
    background: var(--band);
    display: flex; align-items: center; padding-left: 51px;
  }
  .section-band--candle { top: 33px; }
  .section-band--skin { top: 507px; }
  .section-title {
    font-family: "Fraunces", "Georgia", serif;
    font-weight: 600; font-size: 24.4px; letter-spacing: -0.4px;
    color: var(--ink); line-height: 1; white-space: nowrap;
  }
  .ingredient-list { position: absolute; left: 51px; width: 716px; }
  .ingredient-list--candle { top: 90px; }
  .ingredient-list--skin { top: 564px; }
  .ingredient { margin-bottom: 4.5px; }
  .ingredient-name {
    font-family: "Montserrat", sans-serif; font-weight: 700;
    font-size: 14.4px; line-height: 21px; letter-spacing: 0.2px;
    color: var(--ink); margin-bottom: 1.5px; white-space: nowrap;
  }
  .ingredient-desc {
    font-family: "Montserrat", sans-serif; font-weight: 400;
    font-size: 11.6px; line-height: 17px; color: var(--body-ink);
  }
  .stray-mark {
    position: absolute; left: 51px; top: 489px;
    font-family: "Montserrat", sans-serif; font-size: 11px; color: var(--body-ink);
  }
</style>
</head>
<body>
<main class="sheet">
  <header class="section-band section-band--candle">
    <h1 class="section-title">Ingredients – Candle Collection</h1>
  </header>
  <section class="ingredient-list ingredient-list--candle">
    <article class="ingredient">
      <h2 class="ingredient-name">Soy Wax</h2>
      <p class="ingredient-desc">Soy wax is a natural vegetable wax derived from soybeans. It burns cleanly with minimal soot and offers an excellent hot and cold scent throw. As a renewable and biodegradable wax, soy wax ensures a smooth, even burn and supports environmentally conscious production.</p>
    </article>
    <article class="ingredient">
      <h2 class="ingredient-name">Coconut Wax</h2>
      <p class="ingredient-desc">Coconut wax is made from the oil of sustainably harvested coconuts. Known for its luxurious, creamy appearance, it enhances scent diffusion and burns cooler and longer than many other waxes. Vegan-friendly and eco-conscious, it provides a soft, smooth finish to our candle blends.</p>
    </article>
    <article class="ingredient">
      <h2 class="ingredient-name">Tasmanian Leatherwood Beeswax</h2>
      <p class="ingredient-desc">Wild-sourced from Tasmania, this premium beeswax adds natural structure and hardness to our candles. It burns brightly and cleanly while releasing a gentle, honey-like aroma. Beeswax is naturally purifying and contributes to a longer burn time. We use Leatherwood Beeswax for its exceptional quality and connection to Tasmanian provenance.</p>
    </article>
    <article class="ingredient">
      <h2 class="ingredient-name">Natural Cotton / Wooden Wicks</h2>
      <p class="ingredient-desc">Our candles are wicked using lead-free, zinc-free natural cotton wicks or sustainably sourced wooden wicks. Cotton wicks provide a stable, classic burn, while wooden wicks offer an atmospheric soft crackle and modern aesthetic. Both ensure a clean, consistent burn experience.</p>
    </article>
    <article class="ingredient">
      <h2 class="ingredient-name">Premium Fragrance Oils &amp; Essential Oils</h2>
      <p class="ingredient-desc">We use phthalate-free fragrance oils and pure essential oils to create our signature scent profiles. Many scents are inspired by or derived from Tasmanian botanicals including Blue Gum, Pepperberry, Huon Pine and coastal botanicals. All fragrance components are lab-tested for candle safety and clean performance</p>
    </article>
  </section>
  <span class="stray-mark">.</span>

  <header class="section-band section-band--skin">
    <h1 class="section-title">Ingredients – Botanical &amp; Skin Collection</h1>
  </header>
  <section class="ingredient-list ingredient-list--skin">
    <article class="ingredient">
      <h2 class="ingredient-name">Shea Butter</h2>
      <p class="ingredient-desc">Shea butter is extracted from the nut of the shea tree and is rich in fatty acids and vitamins. It softens and hydrates the skin, offering anti-inflammatory and healing benefits. Its emollient properties allow it to soak deeply into the skin, forming a protective moisture barrier.</p>
    </article>
    <article class="ingredient">
      <h2 class="ingredient-name">Tasmanian Leatherwood Beeswax</h2>
      <p class="ingredient-desc">An outstanding natural emollient that hydrates, protects, softens and soothes the skin while helping to retain moisture. We use this beeswax in our balms for its long-lasting protective barrier and ability to relieve irritation.</p>
    </article>
    <article class="ingredient">
      <h2 class="ingredient-name">Tasmanian Olive Oil</h2>
      <p class="ingredient-desc">Tasmanian Olive Oil moisturises the skin by reducing water loss, while its antioxidant content helps protect skin cells from environmental damage. Found in all our soaps, Olive Oil offers nourishing and gentle cleansing properties.</p>
    </article>
    <article class="ingredient">
      <h2 class="ingredient-name">Coconut Oil</h2>
      <p class="ingredient-desc">Coconut oil is easily absorbed and rich in vitamins E and K. Its antifungal, antibacterial and antioxidant properties make it an effective moisturiser suitable for all skin types. In hair care, coconut water promotes cell growth, strengthens strands and supports healthy hair.</p>
    </article>
    <article class="ingredient">
      <h2 class="ingredient-name">Tasmanian Hemp Oil</h2>
      <p class="ingredient-desc">Locally grown and chemical-free, this nourishing oil hydrates without clogging pores. It plumps and firms the skin, while gamma-linolenic acid provides powerful anti-inflammatory benefits and supports cell regeneration. We use Tasmanian Hemp Oil in our balms and skin care range to calm irritation and promote healthy, hydrated skin.</p>
    </article>
    <article class="ingredient">
      <h2 class="ingredient-name">Tasmanian Seaweed Extract</h2>
      <p class="ingredient-desc">Wild harvested in Tasmania’s pristine oceans and processed locally, this high-purity fucoidan extract offers clinically proven soothing, protective and anti-ageing benefits. Extracted from wild Undaria pinnatifida (wakame), it helps defend skin against environmental stressors and UV exposure.</p>
    </article>
    <article class="ingredient">
      <h2 class="ingredient-name">Tasmanian Blue Gum Extract</h2>
      <p class="ingredient-desc">Wild harvested and ethically sourced, this extract offers anti-inflammatory, antibacterial and antiviral benefits. It helps brighten the skin, reduce redness and boost circulation. We use it in our skin care and hair mask for its strengthening, soothing and shine-enhancing qualities. The Tasmanian Blue Gum (Eucalyptus globulus) is Tasmania’s floral emblem.</p>
    </article>
    <article class="ingredient">
      <h2 class="ingredient-name">Sodium Hydroxide (Soap Making Only)</h2>
      <p class="ingredient-desc">Sodium hydroxide (lye) is essential for the saponification process and is not present in the finished product. This reaction between the alkali and oils creates soap and naturally produces glycerin, valued for its humectant properties and ability to hydrate the skin.</p>
    </article>
  </section>
</main>
</body>
</html>
```